Ferncrest Dental, LLC business card project

Business card to be designed with current logo.
Dental office- please keep design of card that looks clean and professional.
Please include the following info:
Ferncrest Dental, LLC
Dr. Lorna Pettigrew
2871 Marlowe Street
Bethlehem, PA 18093
610-555-0193
ferncrestdental.office@examplemail.test
Hello everyone-
Reason: Just got back from overseas- will look at all designs and provide feedback. Thank you!
Reason: Polling my friends for the final selection-
thank you to all those that participated- so many talented designers!

```html
<!DOCTYPE html>
<html lang="en">
<head>
<meta charset="utf-8">
<title>Ferncrest Dental, LLC – Business Card</title>
<link rel="stylesheet" href="https://fonts.googleapis.com/css2?family=Crimson+Pro:wght@400;600&display=swap">
<style>
  :root {
    --page-bg: #e9e7e3;
    --card-white: #ffffff;
    --ink-black: #0c0c0c;
    --brand-green: #7bc62d;
    --swoosh-light: #f2f2f2;
    --swoosh-dark: #4a4f53;
    --text-dark: #141414;
  }
  * { box-sizing: border-box; margin: 0; padding: 0; }
  html, body {
    width: 922px; height: 1200px; overflow: hidden;
    background: var(--page-bg);
    font-family: "Crimson Pro", Georgia, serif;
  }
  .business-card {
    position: absolute; left: 41px; top: 360px;
    width: 840px; height: 480px;
    background: var(--card-white);
    border-radius: 14px; overflow: hidden;
    box-shadow: 0 6px 18px rgba(0,0,0,0.18);
  }
  .card-shapes { position: absolute; inset: 0; }
  .side-name {
    position: absolute; left: 88px; top: 250px;
    writing-mode: vertical-rl;
    font-size: 38px; font-weight: 400; color: var(--brand-green);
    letter-spacing: 0.5px;
  }
  .brand {
    position: absolute; left: 300px; top: 58px;
    display: flex; align-items: center; gap: 14px;
  }
  .brand-dot {
    width: 30px; height: 30px; border-radius: 50%;
    background: var(--brand-green);
  }
  .brand-name {
    font-size: 46px; font-weight: 400; color: var(--brand-green);
    letter-spacing: 0.3px; white-space: nowrap;
  }
  .name-bar {
    position: absolute; left: 440px; top: 172px;
    width: 420px; height: 54px;
    background: var(--ink-black);
    border-radius: 10px;
    display: flex; align-items: center; padding-left: 36px;
    color: var(--card-white); font-size: 30px; font-weight: 600;
  }
  .contact-list { position: absolute; left: 462px; top: 258px; list-style: none; }
  .contact-item {
    display: flex; align-items: flex-start; gap: 12px;
    color: var(--text-dark); font-size: 19px; line-height: 1.25; font-weight: 600;
    margin-bottom: 20px;
  }
  .contact-item svg { flex: none; width: 32px; height: 32px; }
  .contact-item span { padding-top: 4px; }
  .contact-email span { font-size: 17.5px; padding-top: 6px; }
</style>
</head>
<body>
  <div class="business-card">
    <svg class="card-shapes" viewBox="0 0 840 480" width="840" height="480" aria-hidden="true">
      <defs>
        <linearGradient id="swooshShade" x1="0" y1="0" x2="1" y2="1">
          <stop offset="0" stop-color="var(--swoosh-light)"/>
          <stop offset="0.35" stop-color="#9da2a6"/>
          <stop offset="1" stop-color="var(--swoosh-dark)"/>
        </linearGradient>
      </defs>
      <path d="M0 0 H150 C150 110 225 160 300 235 C360 295 382 380 372 480 H0 Z" fill="var(--ink-black)"/>
      <path d="M150 40 C175 120 250 160 318 228 C382 292 406 382 398 480 H372 C382 380 360 295 300 235 C230 165 168 120 150 40 Z" fill="url(#swooshShade)"/>
    </svg>

    <div class="side-name">Ferncrest Dental</div>

    <div class="brand">
      <span class="brand-dot"></span>
      <span class="brand-name">Ferncrest Dental, LLC</span>
    </div>

    <div class="name-bar">Dr. Lorna Pettigrew</div>

    <ul class="contact-list">
      <li class="contact-item contact-address">
        <svg viewBox="0 0 32 32"><path d="M16 4 L2 16 H6 V29 H13 V21 H19 V29 H26 V16 H30 Z" fill="var(--text-dark)"/></svg>
        <span>2871 Marlowe Street<br>Bethlehem, PA 18093</span>
      </li>
      <li class="contact-item contact-email">
        <svg viewBox="0 0 32 32"><rect x="1" y="4" width="30" height="24" rx="4" fill="var(--text-dark)"/><rect x="5" y="9" width="22" height="14" fill="none" stroke="#fff" stroke-width="1.5"/><path d="M5 9 L16 17 L27 9" fill="none" stroke="#fff" stroke-width="1.5"/></svg>
        <span>ferncrestdental.office@examplemail.test</span>
      </li>
      <li class="contact-item contact-phone">
        <svg viewBox="0 0 32 32"><circle cx="16" cy="16" r="14" fill="none" stroke="var(--text-dark)" stroke-width="2.5"/><path d="M11 9 L14 12 L12.5 14.5 C13.5 16.8 15.2 18.5 17.5 19.5 L20 18 L23 21 L21 23.5 C15 23 9 17 8.5 11 Z" fill="var(--text-dark)"/></svg>
        <span>610-555-0193</span>
      </li>
    </ul>
  </div>
</body>
</html>
```